Website Design for my CNC machine Shop.

I need a new website for my Machining Company.

It can be a simple website that acts more like an "Online Business card" I has to highlight the services I provide and give Companies the confidence to engage my services.

I needs it to be a really modern or even a little futuristic promoting my Company.

I have just moved locations and have renovated the premises and would be great to let everyone know along with a new website.

If you can help with linking it to search engines to help get more exposure that would be great.

It needs to accommodate the three main services I provide which will include capacities of each machine (within that service) and maybe a couple images.
CNC Machining (5-axis, 3-axis)
EDM Wire cutting
3D Metal Printing
Along with home page and Contact page

I have two websites and you can use the txt from either/combination of these.
www.korvanmetalworks.com.au
(no longer do Laser Marking and etching but now do 3D metal Printing)
www.brislotech.com.au

Happy to chat further with the designer

Company logo's provided.

For Images: I am happy to use Pixelgrove and can purchase any images you like
EDM Wire cut
https://www.pixelgrove.com/search/edm-wire-cutting

CNC Machining:
https://www.pixelgrove.com/search/vertical-cnc-machining
Don't use any with engines or motor vehicle parts

3D metal Printing
https://www.pixelgrove.com/search/slm-metal-printing

Target Market(s)

Defence, Aerospace, Medical, HIgh Precision

Industry/Entity Type

Mechanical Engineering

Coding

Coded - Design and coding required

Number of Pages Required

5+ page

Requirements
Must have
• Home page, 3 services, Contacts. Can add image to each of the services

```html
<!DOCTYPE html>
<html lang="en">
<head>
<meta charset="utf-8">
<title>KORVAN Precision Machinists</title>
<link href="https://fonts.googleapis.com/css2?family=Montserrat:wght@400;500;600;700&display=swap" rel="stylesheet">
<style>
:root{
  --green:#3dba86;
  --green-dark:#2fa574;
  --navy:#0f2d45;
  --ink:#111;
  --body:#444;
  --grey-bg:#efefef;
  --white:#fff;
  --star:#f5b301;
}
*{box-sizing:border-box;margin:0;padding:0}
html,body{width:1200px;height:3632px;overflow:hidden}
body{font-family:'Montserrat',sans-serif;color:var(--ink);background:var(--white);position:relative}
.abs{position:absolute}
.btn{position:absolute;background:var(--green);color:var(--white);font-size:13px;font-weight:500;display:flex;align-items:center;justify-content:center;border-radius:4px}
.pill{border-radius:20px}
.heading{font-weight:700;font-size:30px;color:var(--ink);letter-spacing:.2px}
.rule{position:absolute;height:3px;width:54px;background:var(--green)}
.stripes{position:absolute;background:repeating-linear-gradient(90deg,#dcdcdc 0 1px,transparent 1px 8px)}
.stripes-h{position:absolute;background:repeating-linear-gradient(0deg,#dcdcdc 0 1px,transparent 1px 8px)}
.photo{position:absolute}

/* hero */
.hero{position:absolute;left:0;top:0;width:1200px;height:601px;background:linear-gradient(110deg,#10304d 0%,#1f4e74 45%,#5d8fb4 75%,#2c5a80 100%)}
.logo-name{position:absolute;font-weight:700;color:#c9d3dc;letter-spacing:6px}
.logo-sub{position:absolute;color:var(--green);letter-spacing:3px;font-weight:500}
.nav{position:absolute;top:36px;left:557px;display:flex;gap:40px;font-size:13px;color:var(--white)}
.hero h1{position:absolute;left:140px;top:190px;width:480px;font-size:35px;line-height:46px;color:var(--white);font-weight:700}
.hero p{position:absolute;left:142px;top:333px;width:380px;font-size:18px;line-height:28px;color:var(--white)}

/* about */
.about-title{left:653px;top:734px}
.about-lead{position:absolute;left:653px;top:800px;width:400px;font-size:15px;line-height:26px;font-weight:600}
.about-text{position:absolute;left:653px;top:860px;width:420px;font-size:12px;line-height:22px;color:var(--body)}
.dots{position:absolute;left:935px;top:985px;width:175px;height:72px;background:radial-gradient(#d4d4d4 1.2px,transparent 1.4px) 0 0/14px 14px}

/* services */
.services{position:absolute;left:0;top:1213px;width:1200px;height:546px;background:var(--grey-bg)}
.center-title{position:absolute;left:0;width:1200px;text-align:center}
.card{position:absolute;top:149px;width:289px;height:310px}
.card .pic{position:absolute;left:0;top:0;width:289px;height:210px;border:3px solid var(--white)}
.card .panel{position:absolute;left:24px;top:167px;width:243px;height:143px;background:var(--green);color:var(--white);text-align:center}
.card .icon{position:absolute;left:110px;top:-36px;width:68px;height:68px;border-radius:50%;background:var(--white);display:flex;align-items:center;justify-content:center}
.card h3{margin-top:44px;font-size:16px;font-weight:500}
.card p{font-size:12px;line-height:19px;margin:6px 16px 0}
.card a{display:block;font-size:12px;font-weight:600;text-decoration:underline;margin-top:6px;color:var(--white)}

/* why */
.why-title{left:144px;top:1864px}
.why-text{position:absolute;left:142px;top:1930px;width:400px;font-size:12px;line-height:22px;color:var(--body)}
.feature{position:absolute;left:140px;display:flex;align-items:center;gap:16px;font-size:14px;font-weight:600;width:400px;line-height:19px}

/* reviews */
.reviews{position:absolute;left:0;top:2351px;width:1200px;height:593px;background:var(--grey-bg)}
.reviews .intro{position:absolute;left:150px;top:143px;width:900px;text-align:center;font-size:12px;line-height:22px;color:var(--body)}
.review{position:absolute;top:212px;width:290px;height:295px;background:var(--white)}
.review .q{position:absolute;font-size:62px;font-weight:700;color:var(--green);line-height:1}
.review p{position:absolute;left:25px;top:62px;width:245px;font-size:12px;line-height:22px;color:var(--body)}
.review .avatar{position:absolute;left:25px;top:212px;width:62px;height:62px;border-radius:50%;border:2px dashed var(--green);background:#dfe6e3}
.review .name{position:absolute;left:101px;top:222px;font-size:15px;font-weight:500}
.review .stars{position:absolute;left:101px;top:246px;color:var(--star);font-size:14px;letter-spacing:2px}

/* clients */
.client{position:absolute;top:3095px;width:170px;height:103px;background:var(--white);box-shadow:0 4px 14px rgba(0,0,0,.08);display:flex;align-items:center;justify-content:center;gap:8px;font-size:26px;font-weight:600;color:#333}
.client .mark{width:22px;height:22px;border-radius:50%;background:var(--green)}
.arrow{position:absolute;top:3126px;width:40px;height:40px;border-radius:50%;display:flex;align-items:center;justify-content:center}

/* footer */
.footer{position:absolute;left:0;top:3285px;width:1200px;height:308px;background:var(--navy);color:var(--white)}
.footer h4{position:absolute;font-size:16px;font-weight:600}
.footer .ul{position:absolute;height:2px;width:54px;background:var(--green)}
.links{position:absolute;left:142px;top:107px;font-size:12px;line-height:42px}
.contact{position:absolute;left:428px;font-size:12px;line-height:21px;display:flex;gap:10px}
.social{position:absolute;top:174px;width:30px;height:30px;border-radius:50%;border:1.5px solid var(--white)}
.bottom{position:absolute;left:0;top:3593px;width:1200px;height:39px;background:var(--green);color:var(--white);font-size:12px;display:flex;align-items:center;justify-content:center}
</style>
</head>
<body>

<section class="hero">
  <div class="photo" role="img" aria-label="Close-up of a CNC spindle machining a precision aluminium part, blue toned" style="left:560px;top:0;width:640px;height:601px;background:radial-gradient(ellipse at 60% 45%,#b9d3e6 0%,#6e9cbf 35%,rgba(31,78,116,0) 75%)"></div>
  <div class="logo-name" style="left:140px;top:10px;font-size:50px;line-height:60px">KORVAN</div>
  <div class="logo-sub" style="left:141px;top:74px;font-size:13px">PRECISION MACHINISTS</div>
  <nav class="nav"><span>Home</span><span>About Us</span><span>Services</span><span>CNC Machining</span></nav>
  <div class="btn pill" style="left:952px;top:30px;width:107px;height:32px">Contact Us</div>
  <h1>Precision Engineering for Aerospace, Defence, and Medical Industries</h1>
  <p>Precision Engineering for Aerospace, Defence, and Medical Industries</p>
  <div class="btn pill" style="left:141px;top:405px;width:120px;height:35px">Contact Us</div>
</section>

<section>
  <div class="stripes" style="left:495px;top:693px;width:78px;height:300px"></div>
  <div class="stripes-h" style="left:141px;top:1042px;width:200px;height:78px"></div>
  <div class="photo" role="img" aria-label="CNC machine cutting a gear with glowing sparks" style="left:141px;top:691px;width:350px;height:349px;background:linear-gradient(160deg,#cfcfcf,#6b6b6b 55%,#2e2e2e)"></div>
  <div class="photo" role="img" aria-label="Row of machining centres on a workshop floor" style="left:338px;top:880px;width:243px;height:247px;border:3px solid var(--white);background:linear-gradient(180deg,#8a8a7a,#4a5e86 55%,#c2a86a)"></div>
  <h2 class="heading abs about-title">ABOUT US</h2>
  <div class="rule" style="left:653px;top:772px"></div>
  <p class="about-lead">We are an innovative company that specialise in technical and creative engineering</p>
  <p class="about-text">Our core sectors of expertise are in EDM wire cutting, Laser Etching /Marking and CNC machining. With our combination of highly skilled staff and sophisticated machinery we offer a comprehensive and professional service.</p>
  <div class="btn" style="left:653px;top:968px;width:127px;height:42px">Read More</div>
  <div class="dots"></div>
</section>

<section class="services">
  <h2 class="heading center-title" style="top:78px">OUR SERVICES</h2>
  <div class="rule" style="left:573px;top:117px"></div>

  <div class="card" style="left:141px">
    <div class="pic" role="img" aria-label="CNC lathe machine in a workshop" style="background:linear-gradient(150deg,#d0d3d6,#5d6470 60%,#2c3440)"></div>
    <div class="panel">
      <div class="icon"><svg width="36" height="36" viewBox="0 0 36 36" fill="none" stroke="#0f2d45" stroke-width="1.6"><rect x="4" y="6" width="28" height="22" rx="2"/><rect x="10" y="11" width="16" height="11"/><line x1="6" y1="32" x2="30" y2="32"/></svg></div>
      <h3>CNC Machining</h3>
      <p>With our combination of high quality Torvex Machining Centres..</p>
      <a>Read More</a>
    </div>
  </div>
  <div class="card" style="left:456px">
    <div class="pic" role="img" aria-label="EDM wire cutting head over a metal plate" style="background:linear-gradient(160deg,#e2eef7,#8fb3cf 55%,#4d6f8c)"></div>
    <div class="panel">
      <div class="icon"><svg width="36" height="36" viewBox="0 0 36 36" fill="none" stroke="#0f2d45" stroke-width="1.6"><rect x="8" y="10" width="5" height="20"/><rect x="15.5" y="6" width="5" height="24"/><rect x="23" y="10" width="5" height="20"/></svg></div>
      <h3>EDM Wire Cutting</h3>
      <p>We operate Swiss manufactured Velmont EDM Machines...</p>
      <a>Read More</a>
    </div>
  </div>
  <div class="card" style="left:770px">
    <div class="pic" role="img" aria-label="Metal 3D printing laser with sparks" style="background:radial-gradient(circle at 55% 35%,#f4c27a 0%,#8b6a4c 25%,#2d2f33 70%)"></div>
    <div class="panel">
      <div class="icon"><svg width="36" height="36" viewBox="0 0 36 36" fill="none" stroke="#0f2d45" stroke-width="1.6"><rect x="6" y="6" width="24" height="5"/><path d="M15 11h6l-3 6z"/><rect x="9" y="22" width="18" height="5"/><line x1="4" y1="30" x2="32" y2="30"/></svg></div>
      <h3>3D Metal Printing</h3>
      <p>Stemming from an engineering background and are well...</p>
      <a>Read More</a>
    </div>
  </div>
</section>

<section>
  <h2 class="heading abs why-title">WHY CHOOSE US</h2>
  <div class="rule" style="left:144px;top:1904px"></div>
  <p class="why-text">Lorem ipsum dolor sit amet, consectetur adipiscing elit, sed do eiusmod tempor incididunt ut labore et dolore magna aliqua.</p>
  <div class="feature" style="top:1993px"><svg width="46" height="46" viewBox="0 0 46 46" fill="none" stroke="#0f2d45" stroke-width="1.4"><circle cx="23" cy="12" r="7"/><circle cx="12" cy="24" r="5"/><circle cx="34" cy="24" r="5"/><path d="M4 40c0-6 4-10 8-10s8 4 8 10M26 40c0-6 4-10 8-10s8 4 8 10"/><circle cx="36" cy="38" r="5" stroke="#3dba86"/></svg>Focus On Modern Facilities</div>
  <div class="feature" style="top:2064px"><svg width="46" height="46" viewBox="0 0 46 46" fill="none" stroke="#0f2d45" stroke-width="1.4"><rect x="3" y="8" width="40" height="28" rx="2"/><rect x="12" y="14" width="22" height="14"/><line x1="8" y1="40" x2="38" y2="40"/><circle cx="8" cy="14" r="2" stroke="#3dba86"/></svg>Advanced Technology</div>
  <div class="feature" style="top:2135px"><svg width="46" height="46" viewBox="0 0 46 46" fill="none" stroke="#0f2d45" stroke-width="1.4"><circle cx="23" cy="14" r="7" stroke="#3dba86"/><path d="M20 21v5h6v-5M6 24l8 14h18l8-14"/></svg>Tailor-made Solutions For High Precision Industries</div>
  <div class="btn" style="left:141px;top:2209px;width:127px;height:42px">Contact Us</div>

  <div class="stripes" style="left:970px;top:1845px;width:78px;height:180px"></div>
  <div class="stripes-h" style="left:618px;top:2196px;width:193px;height:80px"></div>
  <div class="photo" role="img" aria-label="Laser cutting head above a perforated metal plate" style="left:618px;top:1843px;width:349px;height:350px;background:linear-gradient(180deg,#b6bfc6,#8a97a3 50%,#d7dde2)"></div>
  <div class="photo" role="img" aria-label="Laser beam sparks on dark metal surface" style="left:813px;top:2030px;width:244px;height:247px;border:3px solid var(--white);background:radial-gradient(circle at 50% 80%,#e4f0ff 0%,#5d7ea3 25%,#1c2c44 70%)"></div>
</section>

<section class="reviews">
  <h2 class="heading center-title" style="top:77px">CUSTOMER REVIEWS</h2>
  <div class="rule" style="left:573px;top:117px"></div>
  <p class="intro">Sed ut perspiciatis unde omnis iste natus error sit voluptatem accusantium doloremque laudantium, totam rem aperiam, eaque ipsa quae ab illo inventore veritatis et quasi architecto beatae vitae dicta sunt explicabo.</p>

  <div class="review" style="left:141px">
    <div class="q" style="left:24px;top:16px">&ldquo;</div>
    <p>Duis aute irure dolor in reprehenderit in voluptate velit esse cillum dolore eu et fugiat nulla pariatur. Excepteur sint ut occaecat cupidatat non proident, sunt in culpa qui officia deserunt mollit anim id est laborum.</p>
    <div class="q" style="left:232px;top:170px">&rdquo;</div>
    <div class="avatar" role="img" aria-label="Customer portrait"></div>
    <div class="name">Tom Ashby</div><div class="stars">★★★★★</div>
  </div>
  <div class="review" style="left:457px">
    <div class="q" style="left:24px;top:16px">&ldquo;</div>
    <p>Duis aute irure dolor in reprehenderit in voluptate velit esse cillum dolore eu et fugiat nulla pariatur. Excepteur sint ut occaecat cupidatat non proident, sunt in culpa qui officia deserunt mollit anim id est laborum.</p>
    <div class="q" style="left:232px;top:170px">&rdquo;</div>
    <div class="avatar" role="img" aria-label="Customer portrait"></div>
    <div class="name">Kara Whitfield</div><div class="stars">★★★★★</div>
  </div>
  <div class="review" style="left:769px">
    <div class="q" style="left:24px;top:16px">&ldquo;</div>
    <p>Duis aute irure dolor in reprehenderit in voluptate velit esse cillum dolore eu et fugiat nulla pariatur. Excepteur sint ut occaecat cupidatat non proident, sunt in culpa qui officia deserunt mollit anim id est laborum.</p>
    <div class="q" style="left:232px;top:170px">&rdquo;</div>
    <div class="avatar" role="img" aria-label="Customer portrait"></div>
    <div class="name">Jon Pereira</div><div class="stars">★★★★★</div>
  </div>
</section>

<section>
  <h2 class="heading center-title" style="top:3020px">OUR CLIENTS</h2>
  <div class="rule" style="left:573px;top:3060px"></div>
  <div class="arrow" style="left:87px;border:1.5px solid #333"><svg width="16" height="12" viewBox="0 0 16 12" fill="none" stroke="#333" stroke-width="1.5"><path d="M15 6H1M6 1L1 6l5 5"/></svg></div>
  <div class="client" style="left:141px"><span class="mark"></span>quarro</div>
  <div class="client" style="left:328px"><span class="mark"></span>vellix</div>
  <div class="client" style="left:515px"><span class="mark"></span>brisca</div>
  <div class="client" style="left:702px"><span class="mark"></span>ondara</div>
  <div class="client" style="left:889px"><span class="mark"></span>telvo</div>
  <div class="arrow" style="left:1072px;background:var(--green)"><svg width="16" height="12" viewBox="0 0 16 12" fill="none" stroke="#fff" stroke-width="1.5"><path d="M1 6h14M10 1l5 5-5 5"/></svg></div>
</section>

<footer class="footer">
  <h4 style="left:142px;top:70px">QUICK LINKS</h4>
  <div class="ul" style="left:142px;top:94px"></div>
  <div class="links">+ Home<br>+ About Us<br>+ Services<br>+ Contact Us</div>

  <h4 style="left:428px;top:70px">CONTACT DETAILS</h4>
  <div class="ul" style="left:428px;top:94px"></div>
  <div class="contact" style="top:109px"><svg width="16" height="20" viewBox="0 0 16 20" fill="none" stroke="#fff" stroke-width="1.5"><path d="M8 19s6-7 6-11A6 6 0 002 8c0 4 6 11 6 11z"/><circle cx="8" cy="8" r="2"/></svg><span>Unit 4, 18-22 Ferntree Way,<br>DARLOW, VIC 3811</span></div>
  <div class="contact" style="top:166px"><svg width="16" height="12" viewBox="0 0 16 12" fill="none" stroke="#fff" stroke-width="1.5"><rect x="1" y="1" width="14" height="10"/><path d="M1 1l7 6 7-6"/></svg><span>info@korvanmetalworks.com.au</span></div>
  <div class="contact" style="top:201px"><svg width="16" height="16" viewBox="0 0 16 16" fill="none" stroke="#fff" stroke-width="1.5"><rect x="1" y="3" width="5" height="12"/><rect x="7" y="1" width="8" height="14"/></svg><span>03 9555 0182</span></div>
  <div class="contact" style="top:236px"><svg width="16" height="16" viewBox="0 0 16 16" fill="none" stroke="#fff" stroke-width="1.5"><path d="M3 1l3 3-2 2c1 3 3 5 6 6l2-2 3 3-2 2C6 15 1 10 1 3z"/></svg><span>+61 400 555 219</span></div>

  <div class="logo-name" style="left:820px;top:60px;font-size:56px;line-height:66px;color:#c9d3dc">KORVAN</div>
  <div class="logo-sub" style="left:821px;top:131px;font-size:14px">PRECISION MACHINISTS</div>
  <div class="social" style="left:886px" aria-label="Social profile link"></div>
  <div class="social" style="left:925px" aria-label="Social profile link"></div>
  <div class="social" style="left:964px" aria-label="Social profile link"></div>
</footer>
<div class="bottom">© 2024 KORVAN Precision Machinists. All Rights Reserved.</div>

</body>
</html>
```